Salon and Spa Distributor Business Card

Need a business card. We are are distributor in the salon and spa industry. We identify with natural beauty. Need a card with:
Company Name: Petal Haven"
Title: "President & CEO"
Address
Company Phone number
email
website
Tag Line:" Naturally Sourced for Salons"

Industry/Entity Type

Business

Contact Information for Business Card

Name: Lena Morcott
Title: "President & CEO"
Address: 317 Birchfield Ln, Oakvane, NJ 07481
Company Phone number: 800-463-9152
email: lenamorcott@petalhaven-example.com
website: www.petalhaven-example.com

Requirements
Should not have
• No black backgrounds

```html
<!DOCTYPE html>
<html lang="en">
<head>
<meta charset="utf-8">
<title>Petal Haven – Business Card</title>
<link rel="stylesheet" href="https://fonts.googleapis.com/css2?family=Mulish:wght@400;600;700&display=swap">
<style>
  :root {
    --bg: #efefef;
    --paper: #f7f7f5;
    --green: #3f9a35;
    --green-light: #5cb13a;
    --green-dark: #2f7f2c;
    --grey: #9a9a9a;
    --white: #ffffff;
  }
  * { margin: 0; padding: 0; box-sizing: border-box; }
  html, body {
    width: 1200px; height: 900px; overflow: hidden;
    background: var(--bg);
    font-family: "Mulish", sans-serif;
  }
  .stage {
    position: relative; width: 1200px; height: 900px;
    display: flex; align-items: center; justify-content: center; gap: 40px;
  }
  .card {
    position: relative; width: 540px; height: 308px; overflow: hidden;
    box-shadow: 0 2px 6px rgba(0,0,0,0.08);
  }
  /* Front side */
  .card-front { background: var(--paper); }
  .holder { position: absolute; left: 34px; top: 30px; }
  .holder-name { color: var(--green); font-size: 22px; font-weight: 700; }
  .holder-title { color: var(--grey); font-size: 15px; margin-top: 2px; }
  .contacts { position: absolute; left: 34px; top: 122px; list-style: none; }
  .contacts li {
    display: flex; align-items: center; gap: 8px;
    color: var(--grey); font-size: 13px; line-height: 22px;
  }
  .contacts svg { width: 12px; height: 12px; flex: none; }
  .brand { position: absolute; display: flex; align-items: center; gap: 10px; }
  .brand-front { left: 304px; top: 92px; }
  .brand-dot { width: 34px; height: 34px; border-radius: 50%; background: var(--green-light); }
  .brand-name { font-size: 26px; font-weight: 400; color: var(--green-light); }
  .address {
    position: absolute; right: 30px; top: 176px; text-align: right;
    color: var(--grey); font-size: 13px; line-height: 18px;
  }
  .address strong { font-weight: 700; }
  .swoosh { position: absolute; left: 0; bottom: 0; width: 540px; height: 110px; }
  .swoosh-url {
    position: absolute; right: 24px; bottom: 12px;
    color: var(--white); font-size: 14px; font-weight: 600;
  }
  /* Back side */
  .card-back {
    background: linear-gradient(150deg, var(--green-dark) 0%, var(--green) 45%, var(--green-light) 100%);
  }
  .brand-back { left: 50%; top: 50%; transform: translate(-50%, -50%); flex-direction: column; gap: 8px; }
  .brand-back .brand-row { display: flex; align-items: center; gap: 12px; }
  .brand-back .brand-dot { width: 42px; height: 42px; background: var(--white); }
  .brand-back .brand-name { color: var(--white); font-size: 32px; }
  .tagline { color: var(--white); font-size: 13px; letter-spacing: 0.5px; white-space: nowrap; }
</style>
</head>
<body>
<main class="stage">
  <section class="card card-front">
    <div class="holder">
      <div class="holder-name">Lena Morcott</div>
      <div class="holder-title">President &amp; CEO</div>
    </div>
    <ul class="contacts">
      <li><svg viewBox="0 0 12 12"><path d="M2 1h2.5l1 2.5-1.5 1a6 6 0 0 0 3.5 3.5l1-1.5 2.5 1V11A9 9 0 0 1 1 2z" fill="#3f9a35"/></svg>800-463-9152</li>
      <li><svg viewBox="0 0 12 12"><rect x="0.5" y="2" width="11" height="8" fill="#3f9a35"/><path d="M0.5 2l5.5 4.5L11.5 2" stroke="#f7f7f5" fill="none"/></svg>lenamorcott@petalhaven-example.com</li>
      <li><svg viewBox="0 0 12 12"><circle cx="6" cy="6" r="5.2" fill="none" stroke="#3f9a35" stroke-width="1.4"/><path d="M1 6h10M6 1c-2.5 3-2.5 7 0 10M6 1c2.5 3 2.5 7 0 10" stroke="#3f9a35" fill="none" stroke-width="1"/></svg>www.petalhaven-example.com</li>
    </ul>
    <div class="brand brand-front">
      <span class="brand-dot"></span>
      <span class="brand-name">Petal Haven</span>
    </div>
    <div class="address">
      <strong>Petal Haven</strong><br>317 Birchfield Ln<br>Oakvane, NJ 07481
    </div>
    <svg class="swoosh" viewBox="0 0 540 110" preserveAspectRatio="none" aria-hidden="true">
      <path d="M0 10 C120 40 220 70 300 110 L0 110 Z" fill="#5cb13a"/>
      <path d="M0 22 C140 50 260 70 340 80 L540 80 L540 110 L0 110 Z" fill="#3f9a35"/>
      <path d="M0 14 C130 44 240 66 330 78" stroke="#f7f7f5" stroke-width="3" fill="none"/>
    </svg>
    <div class="swoosh-url">www.petalhaven-example.com</div>
  </section>

  <section class="card card-back">
    <div class="brand brand-back">
      <div class="brand-row">
        <span class="brand-dot"></span>
        <span class="brand-name">Petal Haven</span>
      </div>
      <div class="tagline">Naturally Sourced for Salons</div>
    </div>
  </section>
</main>
</body>
</html>
```